Automotive Detailing Company looking for Billboard

We need a highway billboard designed. Our company is summit gleam (www.summitgleam-example.ca). We want the billboard to have:

1. "summitgleam" as in the uploaded files, WITH the underline as shown

2. "summitgleam" must be large and about 30-40% of the billboard available space

3. Include KROVA and Glazeshield logos on the billboard as these are the brands we use. Keep in mind we USE these brands and only are marketing that we USE them, and it is not a billboard to promote the brands beyond that we use them. The main thing we are marketing is "summitgleam"

4. Include "Fort McMurray" in the billboard. This billboard will be displayed approx. 250km from our business location.

5. Include mandatory key words "ceramic coating" "paint protection film" "undercarriage restoration" "polishing" "tint" "steam"

6. You can use one of our vehicle photos attached, however, it is not necessary and only provided for inspiration and an option

7. Include a small Chatterbook and Snapgrid Logo

```html
<!DOCTYPE html>
<html lang="en">
<head>
<meta charset="utf-8">
<title>summitgleam — Highway Billboard</title>
<link rel="stylesheet" href="https://fonts.googleapis.com/css2?family=Questrial&family=Montserrat:wght@600;700&display=swap">
<style>
  :root {
    --stage: #0d0d0d;
    --paper: #ffffff;
    --ink: #1f1a24;
    --plum: #2f1c3d;
    --magenta: #c43aab;
    --pink: #e040c8;
    --violet: #6c66b6;
    --car-red: #e5321d;
    --car-dark: #2a2a2e;
  }
  * { box-sizing: border-box; margin: 0; padding: 0; }
  html, body {
    width: 1200px; height: 1200px; overflow: hidden;
    background: var(--stage);
  }
  .billboard {
    position: absolute; left: 40px; top: 352px;
    width: 1120px; height: 496px;
    background: var(--paper); overflow: hidden;
    font-family: "Montserrat", sans-serif; color: var(--ink);
  }
  .vehicle-photo {
    position: absolute; left: 0; top: 0; width: 640px; height: 414px;
    background:
      linear-gradient(172deg, #3a3a3e 0%, #5c5c60 14%, var(--car-dark) 26%, #e8e8ea 30%, var(--car-red) 38%, #f04a2e 60%, var(--car-red) 78%, #3b2a2a 100%);
    -webkit-mask-image: linear-gradient(90deg, #000 0%, #000 70%, transparent 100%);
    mask-image: linear-gradient(90deg, #000 0%, #000 70%, transparent 100%);
  }
  .wordmark {
    position: absolute; left: 502px; top: 24px;
    font-family: "Questrial", sans-serif; font-size: 90px; line-height: 1;
    color: var(--violet); letter-spacing: 1px;
  }
  .wordmark-rule {
    position: absolute; left: 504px; top: 123px; width: 304px; height: 5px;
    background: var(--pink);
  }
  .tagline {
    position: absolute; left: 579px; top: 138px;
    font-family: "Questrial", sans-serif; font-size: 26px; letter-spacing: 1.5px;
    color: var(--ink);
  }
  .service {
    position: absolute; display: flex; align-items: center; gap: 12px;
    font-size: 22px; font-weight: 600; line-height: 26px; letter-spacing: -0.3px;
    text-transform: uppercase;
  }
  .service svg { width: 50px; height: 50px; flex: none; }
  .service--ceramic { left: 511px; top: 198px; }
  .service--ppf { left: 819px; top: 194px; }
  .service--detail { left: 511px; top: 278px; }
  .service--tint { left: 819px; top: 278px; }
  .keywords {
    position: absolute; left: 511px; top: 345px; width: 600px;
    font-size: 15px; font-weight: 600; letter-spacing: 0.5px;
    color: var(--magenta); text-transform: uppercase; white-space: nowrap;
  }
  .city-tab {
    position: absolute; left: 0; top: 373px; width: 300px; height: 41px;
  }
  .city-tab svg { position: absolute; inset: 0; }
  .city-tab span {
    position: absolute; left: 16px; top: 7px;
    color: #fff; font-size: 24px; font-weight: 700; letter-spacing: 0.3px;
  }
  .partners {
    position: absolute; left: 20px; top: 432px;
    display: flex; align-items: center; gap: 28px;
    font-size: 24px; font-weight: 700; color: var(--ink);
  }
  .partner { display: flex; align-items: center; gap: 10px; }
  .partner-mark { width: 26px; height: 26px; background: var(--magenta); }
  .contact-bands { position: absolute; left: 0; top: 0; width: 1120px; height: 496px; }
  .phone {
    position: absolute; left: 445px; top: 383px;
    display: flex; align-items: center; gap: 10px;
    color: #fff; font-size: 56px; font-weight: 700; letter-spacing: 0.5px; line-height: 70px;
  }
  .phone svg { width: 44px; height: 44px; }
  .socials {
    position: absolute; left: 946px; top: 393px;
    display: flex; flex-direction: column; gap: 4px;
    color: #fff; font-size: 15px; font-weight: 600;
  }
  .socials span { display: flex; align-items: center; gap: 6px; }
  .socials i { width: 9px; height: 9px; border-radius: 50%; background: #fff; display: inline-block; }
  .web-address {
    position: absolute; left: 460px; width: 660px; top: 456px;
    text-align: center; color: #fff; font-size: 27px; font-weight: 700; letter-spacing: 2px;
  }
</style>
</head>
<body>
  <main class="billboard">
    <div class="vehicle-photo" role="img" aria-label="Glossy red sports car hood photographed in a detailing bay"></div>

    <div class="wordmark">summitgleam</div>
    <div class="wordmark-rule"></div>
    <p class="tagline">THE PROFESSIONAL DETAILERS</p>

    <div class="service service--ceramic">
      <svg viewBox="0 0 50 50"><circle cx="25" cy="25" r="24" fill="var(--plum)"/><circle cx="25" cy="25" r="19" fill="none" stroke="#fff" stroke-width="1.5"/><path d="M25 13l10 4v7c0 7-4.5 11-10 13-5.5-2-10-6-10-13v-7z" fill="none" stroke="#fff" stroke-width="2"/></svg>
      <span>Ceramic<br>Coating</span>
    </div>
    <div class="service service--ppf">
      <svg viewBox="0 0 50 50"><circle cx="25" cy="25" r="24" fill="var(--plum)"/><circle cx="25" cy="25" r="19" fill="none" stroke="#fff" stroke-width="1.5"/><path d="M15 29v-4l3-6h14l3 6v4zM18 29v3M32 29v3" fill="none" stroke="#fff" stroke-width="2"/><circle cx="19" cy="26" r="1.5" fill="#fff"/><circle cx="31" cy="26" r="1.5" fill="#fff"/></svg>
      <span>Paint<br>Protection Film</span>
    </div>
    <div class="service service--detail">
      <svg viewBox="0 0 50 50"><circle cx="25" cy="25" r="24" fill="var(--plum)"/><circle cx="25" cy="25" r="19" fill="none" stroke="#fff" stroke-width="1.5"/><circle cx="22" cy="22" r="7" fill="none" stroke="#fff" stroke-width="2"/><path d="M27 27l8 8M22 18v8M18 22h8" stroke="#fff" stroke-width="2"/></svg>
      <span>Interior &amp;<br>Exterior Details</span>
    </div>
    <div class="service service--tint">
      <svg viewBox="0 0 50 50"><circle cx="25" cy="25" r="24" fill="var(--plum)"/><circle cx="25" cy="25" r="19" fill="none" stroke="#fff" stroke-width="1.5"/><path d="M15 34V22l7-7h13v19z" fill="none" stroke="#fff" stroke-width="2"/><path d="M17 22l6-5h10v8H17z" fill="#fff"/></svg>
      <span>Window<br>Tint</span>
    </div>

    <p class="keywords">Polishing • Steam Cleaning • Undercarriage Restoration</p>

    <div class="city-tab">
      <svg viewBox="0 0 300 41" width="300" height="41"><polygon points="0,0 286,0 258,41 0,41" fill="#111"/><polygon points="286,0 300,0 272,41 258,41" fill="var(--magenta)"/></svg>
      <span>FORT MCMURRAY</span>
    </div>

    <div class="partners">
      <span class="partner"><i class="partner-mark"></i>Glazeshield</span>
      <span class="partner">KROVA</span>
    </div>

    <svg class="contact-bands" viewBox="0 0 1120 496">
      <polygon points="434,381 1120,381 1120,454 434,454 417,418" fill="var(--plum)"/>
      <polygon points="440,454 1120,454 1120,496 466,496" fill="var(--magenta)"/>
    </svg>

    <div class="phone">
      <svg viewBox="0 0 44 44"><path d="M12 6l6 8-4 4c2 5 6 9 11 11l4-4 8 6-4 7C21 37 7 23 5 11z" fill="#fff"/><path d="M26 12a8 8 0 0 1 6 6M27 6a14 14 0 0 1 11 11" fill="none" stroke="#fff" stroke-width="2.5" stroke-linecap="round"/></svg>
      <span>(780) 555 0142</span>
    </div>
    <div class="socials">
      <span><i></i>Chatterbook</span>
      <span><i></i>Snapgrid</span>
    </div>

    <p class="web-address">www.summitgleam-example.ca</p>
  </main>
</body>
</html>
```